Canyon Ridge Early Jump Ball Hoops Classic

This is a flyer to advertise a boys & girls basketball tournament. It will be emailed out to various clubs/organizations in the West in attempt to get them to register for the tournament.
I would like it to have black background with a watermark background of the Salt Lake City city scape. The city scape needs to include the Mountains and downtown buildings of SLC. I would also like a pic of a couple basketball players on the flyer

Colors
85cae6
ffffff

Requirements
Must have
• Black background
• Salt Lake City city scape watermark (showing mountains and downtown buildings)
• Use uploaded info
• Use 1 or 2 uploaded basketball player pics
Nice to have
• Use Carolina blue, black, silver & white for colors

```html
<!DOCTYPE html>
<html lang="en">
<head>
<meta charset="utf-8">
<title>Canyon Ridge Early Jump Ball Hoops Classic</title>
<link href="https://fonts.googleapis.com/css2?family=Oswald:wght@400;500;600&family=Lato:wght@400;700&display=swap" rel="stylesheet">
<style>
  :root {
    --carolina: #85cae6;
    --black: #111111;
    --white: #ffffff;
    --silver: #b9bcbf;
    --ink: #1c1c1c;
    --page: #f4f4f4;
  }
  * { margin: 0; padding: 0; box-sizing: border-box; }
  html, body { width: 1200px; height: 1200px; overflow: hidden; background: var(--page); }
  .flyer {
    position: absolute; left: 208px; top: 54px;
    width: 965px; height: 1352px;
    transform: scale(0.8); transform-origin: top left;
    background: var(--white); overflow: hidden;
    font-family: "Lato", sans-serif; color: var(--ink);
  }
  .abs { position: absolute; }
  .text-layer { z-index: 3; }
  .event-name {
    left: 150px; top: 50px; width: 320px; text-align: center;
    font-family: "Oswald", sans-serif; font-weight: 600; font-size: 34px;
    line-height: 1.1; text-transform: uppercase; color: var(--black);
  }
  .hero-band { left: 0; top: 232px; width: 965px; height: 410px; }
  .hero-photo { left: 560px; top: 25px; width: 370px; height: 830px; border-radius: 40px; z-index: 1;
    background: linear-gradient(160deg, #d9b08c 0%, #7fb6d8 45%, #4d8fc4 75%, #3aa7c0 100%); }
  .headline { left: 36px; top: 305px; font-family: "Oswald", sans-serif; text-transform: uppercase; line-height: 1; white-space: nowrap; }
  .headline .kicker { color: var(--carolina); font-size: 52px; font-weight: 500; }
  .headline .title { color: var(--white); font-size: 62px; font-weight: 500; margin-top: 6px; }
  .facts { left: 36px; top: 452px; width: 500px; font-family: "Oswald", sans-serif; font-size: 30px; font-weight: 500; line-height: 47px; text-transform: uppercase; white-space: nowrap; }
  .facts .row { display: flex; gap: 38px; }
  .facts .label { color: var(--carolina); }
  .facts .value { color: var(--white); text-transform: none; }
  .facts .value.caps { text-transform: uppercase; }
  .notes { left: 38px; top: 662px; width: 440px; }
  .notes h2 { font-family: "Oswald", sans-serif; font-weight: 500; color: var(--carolina); font-size: 34px; line-height: 1.1; margin-bottom: 14px; }
  ul.bullets { list-style: none; font-size: 21px; line-height: 26.5px; }
  ul.bullets li { position: relative; padding-left: 15px; margin-bottom: 7px; }
  ul.bullets li::before { content: ""; position: absolute; left: 0; top: 11px; width: 7px; height: 7px; border-radius: 50%; background: var(--carolina); }
  .rules-band { left: 0; top: 889px; width: 965px; height: 288px; background: var(--carolina); }
  .rules { left: 38px; top: 927px; width: 740px; }
  .rules ul.bullets li::before { background: var(--white); }
  .rules a { color: var(--white); font-weight: 700; text-decoration: none; }
  .price-badge { left: 701px; top: 759px; width: 226px; height: 226px; border-radius: 50%; z-index: 4;
    background: var(--black); border: 6px solid var(--carolina); box-shadow: 0 0 0 3px var(--silver);
    display: flex; flex-direction: column; align-items: center; justify-content: center;
    font-family: "Oswald", sans-serif; text-transform: uppercase; text-align: center; line-height: 1; }
  .price-badge .label { color: var(--white); font-size: 26px; margin-bottom: 8px; }
  .price-badge .amount { color: var(--carolina); font-size: 46px; font-weight: 600; line-height: 1.05; }
  .player-photo { left: 790px; top: 1025px; width: 160px; height: 327px; border-radius: 30px 30px 0 0; z-index: 2;
    background: linear-gradient(170deg, #6b4a3a 0%, #8cc6e4 40%, #5b9fd0 80%, #e9e9e9 100%); }
  .venue { left: 42px; top: 1218px; }
  .venue .name { font-family: "Oswald", sans-serif; font-weight: 600; font-size: 30px; text-transform: uppercase; line-height: 1; margin-left: 28px; }
  .venue address { font-style: normal; font-weight: 700; font-size: 15px; line-height: 19px; margin-left: 28px; margin-top: 6px; }
  .contact { left: 343px; top: 1230px; font-size: 21px; font-weight: 700; line-height: 41px; }
  .contact div { display: flex; align-items: center; gap: 8px; }
  .footer-bar { left: 0; top: 1337px; width: 965px; height: 15px; background: var(--black); z-index: 3; }
</style>
</head>
<body>
<main class="flyer">
  <div class="abs event-name">Canyon Ridge Early Jump Ball Hoops Classic</div>

  <svg class="abs hero-band" viewBox="0 232 965 410" width="965" height="410" aria-hidden="true">
    <rect x="0" y="232" width="965" height="7" fill="var(--silver)"/>
    <rect x="0" y="239" width="965" height="395" fill="var(--black)"/>
    <rect x="0" y="634" width="965" height="8" fill="var(--silver)"/>
  </svg>
  <svg class="abs" style="left:0;top:0" width="965" height="720" viewBox="0 0 965 720" aria-hidden="true">
    <polygon points="706,0 965,0 965,712 531,377" fill="var(--silver)"/>
    <polygon points="722,0 965,0 965,700 548,377" fill="var(--carolina)"/>
  </svg>

  <div class="abs hero-photo" role="img" aria-label="Photo of a girl in a light blue uniform dribbling a basketball"></div>

  <div class="abs headline text-layer">
    <div class="kicker">YBU Super Regional</div>
    <div class="title">National Qualifier</div>
  </div>

  <div class="abs facts text-layer">
    <div class="row"><span class="label">Date:</span><span class="value caps">5th TO 6th MAY</span></div>
    <div class="row"><span class="label">Grades:</span><span class="value">Boys &amp; Girls 2nd – 8th</span></div>
    <div class="row"><span class="label">Divisions:</span><span class="value">Div I &amp; Div II</span></div>
  </div>

  <section class="abs notes text-layer">
    <h2>NOTES:</h2>
    <ul class="bullets">
      <li>NATIONAL QUALIFYER</li>
      <li>4 game guarantee</li>
      <li>West Coast Super Regional Event. Already confirmed teams from UT, NV, OR, ID, CO, WY, CA, WA, MT</li>
    </ul>
  </section>

  <div class="abs rules-band"></div>
  <section class="abs rules text-layer">
    <ul class="bullets">
      <li>This event is licensed by the Youth Basketball Union of the U.S., Inc.</li>
      <li>All participants must have a current YBU membership.</li>
      <li>YBU membership may not be included as part of the entry fee to the event.</li>
      <li>YBU membership must be obtained before the competition begins except where the event operator has a laptop available with an internet connection.</li>
      <li>Participants are encouraged to visit the YBU web site <a href="#">www.ybuhoops.org</a> to obtain their membership.</li>
    </ul>
  </section>

  <div class="abs price-badge">
    <span class="label">Register Cost</span>
    <span class="amount">$425/<br>Team</span>
  </div>

  <div class="abs player-photo" role="img" aria-label="Photo of a boy in a light blue uniform running on court"></div>

  <div class="abs venue text-layer">
    <svg class="abs" style="left:0;top:0" width="20" height="28" viewBox="0 0 20 28" aria-hidden="true">
      <path d="M10 1a9 9 0 0 1 9 9c0 7-9 17-9 17S1 17 1 10a9 9 0 0 1 9-9z" fill="var(--carolina)"/>
      <circle cx="10" cy="10" r="3.5" fill="var(--white)"/>
    </svg>
    <div class="name">Full Court Hall</div>
    <address>Summit Play Events Center<br>1820 W. 500 S.<br>Salt Lake City, UT</address>
  </div>

  <div class="abs contact text-layer">
    <div>
      <svg width="16" height="16" viewBox="0 0 24 24" aria-hidden="true"><path d="M6.6 10.8a15 15 0 0 0 6.6 6.6l2.2-2.2a1 1 0 0 1 1-.25 11 11 0 0 0 3.6.6 1 1 0 0 1 1 1V20a1 1 0 0 1-1 1A17 17 0 0 1 3 4a1 1 0 0 1 1-1h3.5a1 1 0 0 1 1 1 11 11 0 0 0 .6 3.6 1 1 0 0 1-.25 1z" fill="var(--carolina)"/></svg>
      <span>(801) 555-0142</span>
    </div>
    <div>
      <svg width="17" height="14" viewBox="0 0 24 18" aria-hidden="true"><rect x="1" y="1" width="22" height="16" rx="2" fill="var(--carolina)"/><path d="M2 2l10 8 10-8" stroke="var(--white)" stroke-width="2" fill="none"/></svg>
      <span>coach@canyonridgehoops.com</span>
    </div>
  </div>

  <div class="abs footer-bar"></div>
</main>
</body>
</html>
```